Premium Fitness Meal Plan Design for VoltaKor (Brand Like PlumQuarry!)

VoltaKor 6 Week Autumn Forge Meal Plan Design (Branded Handout)

πŸ“„ Overview:
We are looking for a professionally designed, branded meal plan handout for our fitness facility, VoltaKor. This meal plan will be used during our upcoming 6 Week Autumn Forge Quest, where members aim to lose body fat, build lean muscle, and improve their energy through nutrition and strength training.

The design should be highly polished, visually engaging, and reflect our brand quality β€” something on par with what you would see from larger national gym chains (e.g., Plum Quarry, K62, Delmar’s Drillyard). This is not just a text document β€” we want it to feel premium, motivating, and easy to follow, ideally something members are excited to reference and share.

🧾 Format & Layout:
Size: Standard 8.5x11 inch format (single or double-sided)

Final Output: Print-ready PDF + editable source files

Orientation: Portrait

Can be designed as either:

One visually organized front-and-back sheet

Or two clean, digestible pages presented as a mini-handout

🎨 Design Style:
Clean, energetic, and transformation-focused

Use brand colors and fonts that feel bold, fresh, and motivating

Include icons, dividers, or visual cues to separate sections (not just blocks of text)

Sections should feel approachable and empowering, not clinical or restrictive

Include room for the VoltaKor logo (provided) at the top and/or footer

πŸ“˜ Content to Include:
The following content should be visually structured and formatted in clear, engaging blocks. We’ll provide this content in a PDF format

1. Header Title:
"VoltaKor 6 Week Autumn Forge Nutrition Blueprint"

2. Introduction (Small Block):
Short blurb about the challenge goals (lose body fat, gain energy, preserve lean muscle mass)

3. Elimination List (Foods to Avoid):
A visually separated section with a list of foods and drinks that should be eliminated or greatly reduced for fat loss

4. Smart Swaps Table:
A side-by-side "Craving vs Swap" table that shows easy alternatives to popular bad habits (e.g., soda β†’ sparkling water)

5. Build-Your-Own Meal Plan Sections:
Organize these into clear categories:

Proteins

Carbs

Fats

Veggies

Extras / Smart Swaps
Use icons, color codes, or visual grids to organize these food lists

6. Tips Section (Optional Bonuses):
Hydration goal

Suggested number of meals

Protein shake recommendation

Meal timing tip

10-min walk after dinner tip

πŸ“¦ Files Provided:

All written content in organized text format

βœ… Deliverables:
Final design in print-ready PDF

Editable source file (AI, PSD, or InDesign preferred)

πŸ™Œ Inspiration:
Design should feel in line with the type of professional print materials used by high-end fitness studios. Clean lines, engaging fonts, and premium layout. We're not looking for clipart or gimmicky stock photos β€” we want the design to reflect the premium, results-driven experience our gym provides.

```html
<!DOCTYPE html>
<html lang="en">
<head>
<meta charset="utf-8">
<title>VoltaKor 6 Week Autumn Forge Nutrition Blueprint</title>
<link rel="stylesheet" href="https://fonts.googleapis.com/css2?family=Oswald:wght@500;600;700&family=Roboto+Condensed:wght@300;400&display=swap">
<style>
  :root {
    --stage: #9c9c9c;
    --page: #060606;
    --yellow: #f7d20f;
    --ink: #f2f2f2;
    --muted: #d9d9d9;
    --heading-font: "Oswald", "Arial Narrow", sans-serif;
    --body-font: "Roboto Condensed", "Arial Narrow", sans-serif;
  }
  * { margin: 0; padding: 0; box-sizing: border-box; }
  html, body { width: 1200px; height: 2208px; overflow: hidden; background: var(--stage); }
  .canvas { position: relative; width: 1200px; height: 2208px; background: var(--stage); }

  .page {
    position: absolute; left: 207px; width: 786px; height: 1014px;
    background: var(--page); overflow: hidden;
    box-shadow: 4px 8px 14px rgba(0,0,0,.35);
  }
  .page--front { top: 67px; }
  .page--back { top: 1130px; }

  .hero-photo {
    position: absolute; right: 0; top: 0; width: 560px; height: 1014px;
    background:
      linear-gradient(90deg, var(--page) 0%, rgba(6,6,6,.6) 30%, rgba(6,6,6,0) 60%),
      linear-gradient(180deg, #6e6e80 0%, #4a4a58 35%, #2a2a33 65%, #141418 100%);
  }
  .corner-wedge { position: absolute; left: 0; top: 0; }

  .brand { position: absolute; color: var(--yellow); text-align: center; }
  .brand__name {
    display: block; font-family: var(--heading-font); font-weight: 700;
    font-size: 70px; line-height: 1; letter-spacing: 1px;
  }
  .brand__tag {
    display: block; font-family: var(--heading-font); font-weight: 600;
    font-size: 10px; letter-spacing: 2.5px; margin-top: 6px;
  }
  .page--front .brand { left: 45px; top: 52px; }
  .page--back .brand { left: 511px; top: 890px; }

  .title {
    position: absolute; left: 45px; top: 205px;
    font-family: var(--heading-font); font-weight: 700; color: var(--yellow);
    font-size: 62px; line-height: 72px; text-transform: uppercase; letter-spacing: .5px;
  }

  .section-heading {
    position: absolute; font-family: var(--heading-font); font-weight: 600;
    color: var(--yellow); font-size: 19px; line-height: 23px; text-transform: uppercase;
  }
  .copy {
    position: absolute; font-family: var(--body-font); font-weight: 300;
    color: var(--ink); font-size: 12.5px; line-height: 15.6px;
  }
  .list { position: absolute; list-style: none; font-family: var(--body-font); font-weight: 300;
    color: var(--ink); font-size: 12.5px; line-height: 15.4px; }
  .list li { position: relative; padding-left: 18px; }
  .list li::before { content: "•"; position: absolute; left: 0; color: var(--muted); }

  .swap-table { position: absolute; left: 45px; top: 779px; border-collapse: collapse;
    font-family: var(--body-font); font-weight: 300; color: var(--ink); font-size: 12.5px; }
  .swap-table td { padding: 0; line-height: 15.4px; vertical-align: top; }
  .swap-table td:first-child { width: 126px; }

  .team-photo {
    position: absolute; left: 394px; top: 0; width: 392px; height: 299px;
    background: linear-gradient(160deg, #3a3f6a 0%, #8a3a4a 40%, #5b4a46 65%, #1c1c22 100%);
  }
  .frame-lines { position: absolute; left: 370px; top: 180px; }
</style>
</head>
<body>
<div class="canvas">

  <section class="page page--front">
    <div class="hero-photo" role="img" aria-label="Photo of a woman lifting a dumbbell overhead in the gym"></div>
    <svg class="corner-wedge" width="786" height="1014" viewBox="0 0 786 1014" aria-hidden="true">
      <polygon points="0,1014 577,981 786,710 786,1014" fill="var(--yellow)"/>
    </svg>

    <div class="brand">
      <span class="brand__name">VoltaKor</span>
      <span class="brand__tag">PERSONAL GROUP TRAINING</span>
    </div>

    <h1 class="title">6 Week Autumn Forge<br>Nutrition Blueprint</h1>

    <h2 class="section-heading" style="left:45px;top:436px;">Foods &amp; Drinks to Eliminate (or Greatly Reduce)</h2>
    <p class="copy" style="left:45px;top:478px;">These are the biggest culprits sabotaging fat loss — highly palatable, calorie-dense, and metabolically disruptive:</p>
    <ul class="list" style="left:45px;top:508px;">
      <li>Sugary drinks (sodas, energy drinks, sweet teas, juice blends)</li>
      <li>Fancy coffee drinks (Frostlattes, sugary creamers, flavor pumps)</li>
      <li>Fast food and fried foods (even “grilled” items often packed with oils)</li>
      <li>Packaged snacks (chips, cookies, granola bars, trail mix with candy)</li>
      <li>Baked goods (donuts, muffins, pastries, bagels with cream cheese)</li>
      <li>Alcohol (especially beer and sugary mixers)</li>
      <li>Processed carbs (white breads, crackers, pasta)</li>
      <li>Cheese-heavy meals (pizza, nachos, quesadillas)</li>
      <li>High-fat deli meats (salami, pepperoni, sausage)</li>
      <li>Sauces and condiments loaded with sugar (ketchup, BBQ sauce, honey mustard)</li>
    </ul>

    <h2 class="section-heading" style="left:45px;top:709px;">Smart Swaps for Fat Loss</h2>
    <p class="copy" style="left:45px;top:749px;">Instead of cutting everything and feeling deprived, make these easy grocery-store swaps that still satisfy cravings without killing your progress:</p>
    <table class="swap-table">
      <tr><td>Craving</td><td>Try This Instead</td></tr>
      <tr><td>Soda</td><td>Sparkling water with lime, Fizzella, or plain water with fruit infusions</td></tr>
      <tr><td>Fancy Coffee</td><td>Coffee with unsweetened almond milk + stevia drops or cinnamon</td></tr>
      <tr><td>Chips</td><td>Rice cakes, roasted chickpeas, or crunchy cucumber with Chilora</td></tr>
      <tr><td>Ice Cream</td><td>Frozen banana blended with protein powder (DIY “nice cream”)</td></tr>
      <tr><td>Candy</td><td>Berries, apples or dark chocolate squares (85%+)</td></tr>
      <tr><td>Pasta</td><td>Zucchini noodles, chickpea pasta, or cauliflower rice</td></tr>
      <tr><td>Pizza</td><td>Egg white wraps or low-carb tortillas with turkey pepperoni and light cheese</td></tr>
      <tr><td>Alcohol</td><td>Limit to 1x/week if needed</td></tr>
      <tr><td>Sandwich Bread</td><td>Sprouta bread, low-carb wraps, or lettuce wraps</td></tr>
      <tr><td>Heavy Sauces</td><td>Mustard, salsa, hot sauce, coconut aminos, Greek yogurt-based dips</td></tr>
    </table>
  </section>

  <section class="page page--back">
    <div class="team-photo" role="img" aria-label="Group photo of smiling members flexing together in the studio"></div>
    <svg class="frame-lines" width="170" height="150" viewBox="0 0 170 150" aria-hidden="true">
      <g stroke="var(--yellow)" stroke-width="2.5" fill="none">
        <line x1="4" y1="6" x2="4" y2="140"/>
        <line x1="11" y1="6" x2="11" y2="140"/>
        <line x1="4" y1="125" x2="160" y2="125"/>
        <line x1="4" y1="132" x2="160" y2="132"/>
      </g>
    </svg>

    <h2 class="section-heading" style="left:45px;top:52px;">Build-Your-Own Meal Plan Guide</h2>
    <p class="copy" style="left:45px;top:100px;width:300px;">Use these fit-friendly food lists to mix &amp; match meals. Your job: choose 1 protein, 1 carb (if desired), and 1 fat or veggie at each meal. Keep it simple, keep it consistent.</p>

    <h2 class="section-heading" style="left:45px;top:160px;">Proteins (Choose 1 per Meal/Snack)</h2>
    <ul class="list" style="left:45px;top:206px;">
      <li>Chicken breast or thighs (air fried or grilled)</li>
      <li>Lean ground beef (90/10 or better)</li>
      <li>Ground turkey or turkey breast</li>
      <li>Center-cut pork chops</li>
      <li>Eggs / Egg whites</li>
      <li>Tuna (canned in water)</li>
      <li>Salmon or white fish</li>
      <li>Shrimp</li>
      <li>Greek yogurt (plain, low sugar)</li>
      <li>Cottage cheese (low-fat)</li>
      <li>Protein powder (whey or plant-based)</li>
      <li>Deli turkey (low-sodium)</li>
    </ul>

    <h2 class="section-heading" style="left:45px;top:457px;">Fats (Add Small Amounts<br>to Meals, 2–4 Servings/Day)</h2>
    <ul class="list" style="left:45px;top:518px;">
      <li>Avocado or guacamole</li>
      <li>Olive oil or avocado oil (cooking or drizzle)</li>
      <li>Nut butters (almond, peanut – natural only)</li>
      <li>Whole eggs</li>
      <li>Nuts (almonds, walnuts – portion controlled)</li>
      <li>Chia seeds or flax seeds</li>
    </ul>

    <h2 class="section-heading" style="left:399px;top:343px;">Carbs (Choose 1–2 Servings per Day,<br>Timed Post-Workout or Morning)</h2>
    <ul class="list" style="left:399px;top:408px;">
      <li>Jasmine or basmati rice (white or brown)</li>
      <li>Sweet potatoes or yams</li>
      <li>Rolled oats or steel cut oats</li>
      <li>Quinoa</li>
      <li>Sprouta bread</li>
      <li>Rice cakes</li>
      <li>Berries (blueberries, raspberries, strawberries)</li>
      <li>Apples / Bananas</li>
      <li>Chickpeas or black beans (in moderation)</li>
    </ul>

    <h2 class="section-heading" style="left:399px;top:578px;">Veggies (Unlimited – Fill Your Plate!)</h2>
    <ul class="list" style="left:399px;top:617px;">
      <li>Spinach, kale, arugula</li>
      <li>Zucchini, asparagus, bell peppers</li>
      <li>Broccoli, cauliflower, green beans</li>
      <li>Cucumber, tomatoes, shredded carrots</li>
      <li>Mixed greens or salad kits (watch the dressing)</li>
    </ul>

    <h2 class="section-heading" style="left:45px;top:687px;">Bonus Tips for Maximum Results</h2>
    <ul class="list" style="left:45px;top:733px;">
      <li>Drink 80–120 oz. water daily — hydration is key for fat loss and muscle performance</li>
      <li>Eat 3–4 meals per day — spaced every 3–4 hours</li>
      <li>Include protein in every meal to stabilize blood sugar and support muscle</li>
      <li>Post-workout meal = protein + carb, no added fats</li>
      <li>Up to, two protein shakes per day is allowed, especially post-workout or on busy days</li>
      <li>Limit “treat” meals to 1 per week (keep it controlled)</li>
    </ul>

    <h2 class="section-heading" style="left:45px;top:868px;">Optional Habits to Stack</h2>
    <ul class="list" style="left:45px;top:903px;">
      <li>Weigh in once per week (same day/time)</li>
      <li>Prep 2–3 proteins and veggies on Sunday</li>
      <li>Keep a visible “YES/NO” food list on the fridge</li>
      <li>Add a short 10-min walk after dinner to boost digestion</li>
    </ul>

    <div class="brand">
      <span class="brand__name">VoltaKor</span>
      <span class="brand__tag">PERSONAL GROUP TRAINING</span>
    </div>
  </section>

</div>
</body>
</html>
```